Business card design

I need my logo on this card, things I need the card to have on it
licensed and insured.
owner operators Milo & Dalton Whitby
my phone number 5550138274
Disaster Recovery, Storm Damage Restoration, Proactive Disaster Plan Management, Roof Repair/Restoration Structural Repair and Reconstruction, Emergency Boarding and Tarping Service, Perimeter Fencing, Emergency Tree Removal,

```html
<!DOCTYPE html>
<html lang="en">
<head>
<meta charset="utf-8">
<title>Harlow's Construction L.L.C – Business Card</title>
<link rel="stylesheet" href="https://fonts.googleapis.com/css2?family=Roboto+Condensed:wght@700&family=Jost:wght@400&display=swap">
<style>
  :root {
    --paper: #f4f4f2;
    --brand-blue: #1592e6;
    --ink: #0f2224;
    --mark-grey: #6e7074;
  }
  * { margin: 0; padding: 0; box-sizing: border-box; }
  html, body {
    width: 1200px;
    height: 685px;
    overflow: hidden;
    background: var(--paper);
  }
  .card {
    position: relative;
    width: 1200px;
    height: 685px;
    background: var(--paper);
    overflow: hidden;
    font-family: "Jost", sans-serif;
    color: var(--ink);
  }
  .card__panel {
    position: absolute;
    inset: 0;
  }
  .brand {
    position: absolute;
    left: 46px;
    top: 0;
    width: 580px;
    height: 685px;
    color: var(--mark-grey);
    font-family: "Jost", sans-serif;
    font-weight: 400;
    text-align: center;
  }
  .brand__square {
    position: absolute;
    left: 225px;
    top: 190px;
    width: 130px;
    height: 130px;
    background: var(--mark-grey);
  }
  .brand__name {
    position: absolute;
    left: 0;
    top: 380px;
    width: 580px;
    font-size: 64px;
    line-height: 1.2;
    letter-spacing: 0;
  }
  .contact {
    position: absolute;
    right: 40px;
    top: 78px;
    text-align: right;
  }
  .contact__owners {
    font-family: "Roboto Condensed", sans-serif;
    font-weight: 700;
    font-size: 48px;
    line-height: 1;
    letter-spacing: 0.5px;
  }
  .contact__phone {
    margin-top: 20px;
    font-size: 41px;
    line-height: 1;
  }
  .services {
    position: absolute;
    right: 40px;
    top: 255px;
    list-style: none;
    text-align: right;
    font-size: 25.5px;
    line-height: 42.3px;
    letter-spacing: 0.5px;
  }
  .credentials {
    position: absolute;
    right: 40px;
    top: 620px;
    font-size: 25.5px;
    line-height: 1;
    letter-spacing: 0.5px;
    text-align: right;
  }
</style>
</head>
<body>
  <main class="card">
    <svg class="card__panel" width="1200" height="685" viewBox="0 0 1200 685" aria-hidden="true">
      <polygon points="0,0 517,0 759,250 637,685 0,685" fill="var(--brand-blue)"/>
    </svg>

    <div class="brand">
      <div class="brand__square"></div>
      <p class="brand__name">Harlow's Construction L.L.C</p>
    </div>

    <header class="contact">
      <h1 class="contact__owners">Milo &amp; Dalton Whitby</h1>
      <p class="contact__phone">555-013-8274</p>
    </header>

    <ul class="services">
      <li>Disaster Recovery</li>
      <li>Perimeter Fencing</li>
      <li>Emergency Tree Removal</li>
      <li>Roof Repair/Restoration</li>
      <li>Storm Damage Restoration</li>
      <li>Proactive Disaster Plan Management</li>
      <li>Structural Repair and Reconstruction</li>
      <li>Emergency Boarding and Tarping Service</li>
    </ul>

    <p class="credentials">Licensed and Insured</p>
  </main>
</body>
</html>
```